Dental office needs a sticker designed for promotions

My dental practice needs a sticker designed to be used on patient bags, promotional items, and give aways like retainer cases. The stickers will be round, 3 inches in diameter. I may have some smaller round stickers printed as will, but will use the same design. The logo should be the primary focus and must use brand colors of red and white. I would like to include our information such as the website (www.kpvsmile-example.com), phone number (555)314-9086, and social media info - Facebook @brightoakdental, Instagram @smiles_at_willow_creek_co.

```html
<!DOCTYPE html>
<html lang="en">
<head>
<meta charset="utf-8">
<title>Kingsport Valley Smiles – Promo Sticker</title>
<link rel="stylesheet" href="https://fonts.googleapis.com/css2?family=Source+Sans+3:wght@400;600;700&display=swap">
<style>
  :root {
    --brand-red: #d42045;
    --cream: #fbeac1;
    --paper: #ffffff;
  }
  html, body {
    margin: 0;
    padding: 0;
    width: 1200px;
    height: 1200px;
    overflow: hidden;
    background: var(--paper);
  }
  .sticker-canvas {
    position: relative;
    width: 1200px;
    height: 1200px;
    font-family: "Source Sans 3", sans-serif;
    color: var(--brand-red);
  }
  .sticker-art {
    position: absolute;
    inset: 0;
  }
  .brand-name {
    position: absolute;
    left: 0;
    width: 1200px;
    top: 350px;
    text-align: center;
    font-weight: 600;
    color: var(--brand-red);
    line-height: 1;
    margin: 0;
  }
  .brand-name .brand-line-main {
    display: block;
    font-size: 72px;
    letter-spacing: 1px;
  }
  .brand-name .brand-line-sub {
    display: block;
    font-size: 46px;
    letter-spacing: 4px;
    margin-top: 16px;
  }
  .contact-list {
    position: absolute;
    left: 0;
    width: 1200px;
    top: 650px;
    margin: 0;
    padding: 0;
    list-style: none;
    text-align: center;
  }
  .contact-item {
    display: flex;
    align-items: center;
    justify-content: center;
    gap: 8px;
  }
  .contact-item--phone {
    font-size: 38px;
    font-weight: 700;
    height: 46px;
  }
  .contact-item--web {
    font-size: 38px;
    font-weight: 700;
    letter-spacing: 1.5px;
    height: 46px;
  }
  .contact-item--social {
    font-size: 30px;
    font-weight: 400;
    height: 38px;
    margin-top: 6px;
  }
  .contact-item--web + .contact-item--social {
    margin-top: 12px;
  }
  .icon {
    flex: none;
    fill: var(--brand-red);
  }
  .social-square {
    width: 20px;
    height: 20px;
    border-radius: 3px;
    background: var(--brand-red);
    flex: none;
  }
</style>
</head>
<body>
<main class="sticker-canvas">
  <svg class="sticker-art" width="1200" height="1200" viewBox="0 0 1200 1200" aria-hidden="true">
    <defs>
      <clipPath id="sticker-clip">
        <circle cx="598" cy="581" r="360"/>
      </clipPath>
    </defs>
    <circle cx="598" cy="581" r="360" fill="var(--paper)"/>
    <g clip-path="url(#sticker-clip)">
      <path class="cream-band"
            d="M230,585 C340,520 470,530 620,575 C760,615 880,630 975,480 L975,960 L230,960 Z"
            fill="var(--cream)"/>
      <path class="wave-stripe" d="M230,590 C340,535 460,540 600,575 C740,612 880,640 975,560"
            fill="none" stroke="var(--paper)" stroke-width="7"/>
      <path class="wave-stripe" d="M545,538 C680,590 820,620 975,575"
            fill="none" stroke="var(--paper)" stroke-width="6"/>
      <path class="wave-stripe" d="M560,560 C700,610 860,650 975,588"
            fill="none" stroke="var(--paper)" stroke-width="6"/>
    </g>
    <circle cx="598" cy="581" r="360" fill="none" stroke="var(--brand-red)" stroke-width="1.5"/>
  </svg>

  <h1 class="brand-name">
    <span class="brand-line-main">Kingsport Valley</span>
    <span class="brand-line-sub">SMILES</span>
  </h1>

  <ul class="contact-list">
    <li class="contact-item contact-item--phone">
      <svg class="icon" width="26" height="32" viewBox="0 0 24 30" aria-hidden="true">
        <path d="M5 2 L9 2 L10 9 L7 11 C8 16 11 21 15 24 L18 22 L23 26 L21 29 C12 28 3 17 2 6 Z"/>
      </svg>
      <span>(555) 314-9086</span>
    </li>
    <li class="contact-item contact-item--web">
      <svg class="icon" width="28" height="28" viewBox="0 0 28 28" aria-hidden="true">
        <g fill="none" stroke="var(--brand-red)" stroke-width="2">
          <circle cx="14" cy="14" r="12"/>
          <ellipse cx="14" cy="14" rx="5.5" ry="12"/>
          <line x1="2" y1="14" x2="26" y2="14"/>
          <path d="M4.5 8 H23.5 M4.5 20 H23.5"/>
        </g>
      </svg>
      <span>www.kpvsmile-example.com</span>
    </li>
    <li class="contact-item contact-item--social">
      <span class="social-square" aria-hidden="true"></span>
      <span>@brightoakdental</span>
    </li>
    <li class="contact-item contact-item--social">
      <span class="social-square" aria-hidden="true"></span>
      <span>@smiles_at_willow_creek_co</span>
    </li>
  </ul>
</main>
</body>
</html>
```